Re-brand our business and design!

We need a simple informational website (editable for in the future use)
We need our logo(we have included logo), name, who we are, and what we do displayed.

This is our current site (which is not acceptable, and only a template site): all our information is on this site, please use it forreferanceofinformation.
Www.brightlanefixers.com

Target Market(s)

Real estate brokers, and realtors,homeowners, and anyone looking for home repairs.

Industry/Entity Type

Business

Number of Pages Required

4 page

Font styles to use
Sans Serif

Requirements
Must have
• Our name, contact info, services, and our logo (which we will Email upon request)
• MUST have originality to the site.
• custom "contact us form" or request an estimate form.
Nice to have
• page for real customer testimonies.
• page for our previous work where we can upload pics of completed jobs.
Should not have
• any infringements on any copyrights or plagiarism at all.

```html
<!DOCTYPE html>
<html lang="en">
<head>
<meta charset="utf-8">
<title>Bright Lane Fixers</title>
<link rel="stylesheet" href="https://fonts.googleapis.com/css2?family=Oxygen:wght@400;700&family=Open+Sans:wght@400;600;700&display=swap">
<style>
:root{
  --red:#e30e0e;
  --red-bright:#ff2424;
  --ink:#111111;
  --text:#555555;
  --topbar:#7b7b7b;
  --light:#f2f2f2;
  --footer:#2e2e2e;
  --footer-base:#454545;
  --white:#ffffff;
}
*{margin:0;padding:0;box-sizing:border-box}
html,body{width:1200px;height:2222px;overflow:hidden}
body{position:relative;background:var(--white);font-family:"Open Sans",Arial,sans-serif;color:var(--text)}
.abs{position:absolute}
.heading{font-family:"Oxygen","Open Sans",sans-serif}

/* top bar */
.topbar{left:0;top:0;width:1200px;height:33px;background:var(--topbar);color:var(--white);font-size:13px}
.topbar .address{left:48px;top:8px;display:flex;align-items:center;gap:6px}
.topbar .social{right:32px;top:6px;display:flex;gap:4px}
.topbar .social span{width:19px;height:19px;border-radius:50%;background:var(--white);display:block}

/* header */
.header{left:0;top:33px;width:1200px;height:120px;background:linear-gradient(100deg,#fafafa,#f1f1f1)}
.brand{left:46px;top:47px;font-family:"Oxygen",sans-serif;font-weight:700;font-size:21px;color:var(--ink);display:flex;align-items:center;gap:9px;white-space:nowrap}
.brand i{width:15px;height:15px;background:var(--red);display:block}
.contact-item{top:45px;display:flex;align-items:center;gap:16px}
.contact-item small{display:block;font-size:8px;letter-spacing:1px;color:#666;text-transform:uppercase}
.contact-item b{display:block;font-size:14px;font-weight:600;color:#333;margin-top:2px}

/* nav */
.nav{left:0;top:153px;width:1200px;height:47px;background:var(--ink);z-index:3}
.nav ul{list-style:none;display:flex;position:absolute;left:59px;top:0;height:47px}
.nav li{color:var(--white);font-family:"Oxygen",sans-serif;font-weight:700;font-size:15px;line-height:47px;padding:0 30px}
.nav li.active{background:var(--red);clip-path:polygon(10% 0,100% 0,90% 100%,0 100%);padding:0 31px}
.nav .quote{right:67px;top:0;height:47px;width:182px;background:var(--red);color:var(--white);font-family:"Oxygen",sans-serif;font-weight:700;font-size:14px;line-height:47px;text-align:center;clip-path:polygon(0 0,100% 0,92% 100%,0 100%)}

/* hero */
.hero{left:0;top:153px;width:1200px;height:568px;background:linear-gradient(120deg,#5d4f44 0%,#7a5a40 30%,#a26a4a 55%,#6f5a4c 80%,#5a4c44 100%)}
.hero .shade{inset:0;background:rgba(30,25,22,.45)}
.hero-title{left:59px;top:452px;color:var(--white);font-family:"Oxygen",sans-serif;font-weight:700;font-size:38px;line-height:45px;z-index:2}
.quick-form{left:841px;top:318px;width:282px;height:313px;background:var(--white);z-index:2}
.quick-form .bar{left:12px;top:-8px;width:258px;height:55px;background:var(--red);color:var(--white);font-family:"Oxygen",sans-serif;font-weight:700;font-size:27px;text-align:center;line-height:55px}
.field{position:absolute;left:12px;width:258px;height:42px;border:1px solid #cfcfcf;border-radius:3px;font-size:14px;color:#999;padding:10px 10px}
.submit{left:17px;top:250px;width:108px;height:41px;background:var(--ink);color:var(--white);font-family:"Oxygen",sans-serif;font-weight:700;font-size:17px;text-align:center;line-height:41px;border-radius:2px}

/* about */
.about-photo{left:59px;top:776px;width:388px;height:380px;background:linear-gradient(135deg,#e8dccb 0%,#cdb08a 50%,#a77b4e 100%)}
.about-photo .ad{left:6px;top:100px;font-family:"Oxygen",sans-serif;font-weight:700;color:#222;font-size:19px;line-height:24px;text-align:center;width:240px}
.about-photo .ad span{display:block;font-size:17px;color:#444}
.about-title{left:498px;top:767px;font-size:38px;font-weight:400;color:var(--ink)}
.about-copy{left:500px;top:832px;width:663px;font-size:15px;line-height:22px}
.about-copy p{margin-bottom:22px}
.btn-red{left:495px;top:1117px;width:98px;height:39px;background:var(--red);color:var(--white);font-size:15px;text-align:center;line-height:39px;border-radius:2px}

/* services */
.services{left:0;top:1238px;width:1200px;height:638px;background:var(--light)}
.services-title{left:0;top:1298px;width:1200px;text-align:center;font-size:40px;color:var(--ink)}
.services-sub{left:0;top:1350px;width:1200px;text-align:center;font-size:13px}
.card{top:1407px;width:314px;height:387px;background:var(--white);border:1px solid #cfcfcf}
.card .photo{left:0;top:0;width:312px;height:210px}
.card h3{position:absolute;left:14px;top:220px;font-family:"Oxygen",sans-serif;font-weight:700;font-size:22px;color:var(--red)}
.card p{position:absolute;left:14px;top:256px;width:286px;font-size:13px;line-height:18px}
.card .btn-dark{left:14px;top:323px;width:95px;height:38px;background:var(--ink);color:var(--white);font-size:14px;text-align:center;line-height:38px;border-radius:2px}

/* footer */
.footer{left:0;top:1876px;width:1200px;height:305px;background:var(--footer);color:var(--white)}
.footer .brand-mark{left:62px;top:94px;font-family:"Oxygen",sans-serif;font-weight:700;font-size:19px;white-space:nowrap}
.footer .about-text{left:60px;top:144px;width:290px;font-size:14px;line-height:19px;color:#ddd}
.footer h4{position:absolute;top:34px;font-family:"Oxygen",sans-serif;font-weight:700;font-size:19px}
.footer .links{left:382px;top:72px;list-style:none;font-size:13px;font-weight:700}
.footer .links li{margin-bottom:14px;text-transform:uppercase}
.footer .links li.active{color:var(--red-bright)}
.detail{left:572px;display:flex;gap:14px;font-size:13px}
.detail .ico{width:26px;height:26px;border-radius:50%;background:var(--red-bright);flex:none;display:flex;align-items:center;justify-content:center}
.detail b{display:block;font-size:13px}
.detail span{display:block;font-size:12px;line-height:16px}
.newsletter{left:849px;top:72px;width:296px;font-size:13px;line-height:23px}
.email-box{left:852px;top:143px;width:290px;height:45px;border:1px solid #777;font-size:13px;padding:12px 14px}
.signup{left:852px;top:210px;width:290px;height:45px;background:var(--red-bright);font-family:"Oxygen",sans-serif;font-weight:700;font-size:14px;text-align:center;line-height:45px}
.copyright{left:0;top:2181px;width:1200px;height:41px;background:var(--footer-base);color:var(--white);font-size:12px;text-align:center;line-height:41px}
</style>
</head>
<body>

<div class="abs topbar">
  <div class="abs address">
    <svg width="11" height="14" viewBox="0 0 11 14"><path d="M5.5 0A5.5 5.5 0 0 0 0 5.5C0 9.5 5.5 14 5.5 14S11 9.5 11 5.5A5.5 5.5 0 0 0 5.5 0z" fill="#fff"/><circle cx="5.5" cy="5.3" r="2" fill="#7b7b7b"/></svg>
    18, Harbor Row-42, Riverton
  </div>
  <div class="abs social"><span></span><span></span><span></span><span></span></div>
</div>

<header class="abs header">
  <div class="abs brand"><i></i>Bright Lane Fixers</div>
  <div class="abs contact-item" style="left:714px">
    <svg width="24" height="34" viewBox="0 0 24 34"><rect x="2" y="1" width="20" height="32" rx="3" fill="none" stroke="#666" stroke-width="1.5"/><line x1="2" y1="6" x2="22" y2="6" stroke="#666" stroke-width="1.2"/><line x1="2" y1="27" x2="22" y2="27" stroke="#666" stroke-width="1.2"/><circle cx="12" cy="30" r="1.3" fill="#666"/></svg>
    <div><small>Call us today</small><b>555-201-4477</b></div>
  </div>
  <div class="abs contact-item" style="left:908px">
    <svg width="32" height="30" viewBox="0 0 32 30"><path d="M2 12 16 2l14 10v16H2z" fill="none" stroke="#666" stroke-width="1.5"/><path d="M2 12l14 10 14-10" fill="none" stroke="#666" stroke-width="1.5"/><rect x="7" y="7" width="18" height="10" fill="none" stroke="#666" stroke-width="1.2"/></svg>
    <div><small>Email us now</small><b>Mara@brightlanefixers.com</b></div>
  </div>
</header>

<nav class="abs nav">
  <ul>
    <li class="active">HOME</li><li>ABOUT</li><li>SERVICES</li><li>PROJECTS</li><li>BLOG</li><li>CONTACT</li>
  </ul>
  <div class="abs quote">REQUEST A QUOTE</div>
</nav>

<section class="abs hero" role="img" aria-label="Hands holding a small wooden house over a table covered with home repair tools">
  <div class="abs shade"></div>
</section>
<h1 class="abs hero-title">WELCOME IN<br>BRIGHT LANE FIXERS</h1>

<form class="abs quick-form">
  <div class="abs bar">Contact Now</div>
  <div class="field" style="top:68px">Your Name</div>
  <div class="field" style="top:118px">Your Email</div>
  <div class="field" style="top:167px;height:72px">Message</div>
  <div class="abs submit">Submit</div>
</form>

<section>
  <div class="abs about-photo" role="img" aria-label="Smiling repairman in a blue shirt and tool belt giving an okay sign in a bright room">
    <div class="abs ad">Bright Lane Fixers<span>Call: 555-201-4477<br>Www.brightlanefixers.com</span></div>
  </div>
  <h2 class="abs heading about-title">Why Bright Lane Fixers</h2>
  <div class="abs about-copy">
    <p>Lorem ipsum dolor sit amet, coetuer adipiscing elit. Praesent vestibulum molestie lacus. Aenean dis parturient montes, nascetur ridiculus mus. Lorem ipsum dolor sit amet, coetuer adipiscing elit. Praesent vestibulum molestie lacus. Aenean dis parturient montes, nascetur ridiculus mus. Lorem ipsum dolor sit amet, coetuer adipiscing elit. Praesent vestibulum molestie lacus. Aenean dis parturient montes, nascetur ridiculus mus.</p>
    <p>Lorem ipsum dolor sit amet, coetuer adipiscing elit. Praesent vestibulum molestie lacus. Aenean dis parturient montes, nascetur ridiculus mus. Lorem ipsum dolor sit amet, coetuer adipiscing elit. Praesent vestibulum molestie lacus.</p>
    <p>Lorem ipsum dolor sit amet, coetuer adipiscing elit. Praesent vestibulum molestie lacus. Aenean dis parturient montes, nascetur ridiculus mus.</p>
  </div>
  <div class="abs btn-red">Read More</div>
</section>

<section class="abs services"></section>
<h2 class="abs heading services-title">Our Services</h2>
<p class="abs services-sub">Bathrooms, Kitchens, Washer/Dryer Hook Up Clogged</p>

<article class="abs card" style="left:59px">
  <div class="abs photo" role="img" aria-label="Hands drilling into a wooden frame on a carpentry bench" style="background:linear-gradient(135deg,#d9c3a0,#a88457 60%,#5f6a4f)"></div>
  <h3>Carpentry</h3>
  <p>Stairs, Floors, Decks, Fences Storage sheds, Storage shelving and doorsVapor barrier repair/installation, Attic and crawl</p>
  <div class="abs btn-dark">Read More</div>
</article>
<article class="abs card" style="left:443px">
  <div class="abs photo" role="img" aria-label="Plumbing tools, pipes, a red valve and a pipe wrench" style="background:linear-gradient(135deg,#c9c4bd,#9a8f86 50%,#b03a2a)"></div>
  <h3>Plumbing</h3>
  <p>Bathrooms, Kitchens, Washer/Dryer Hook Up Clogged drains, Toilets, Tubs/Showers Sinks, Garbage disposals, Leaking faucets</p>
  <div class="abs btn-dark">Read More</div>
</article>
<article class="abs card" style="left:827px">
  <div class="abs photo" role="img" aria-label="White front door and window on a house facade with a small potted tree" style="background:linear-gradient(180deg,#b46a55 0%,#e8eaec 18%,#d9dde0 70%,#9aa29a)"></div>
  <h3>Doors &amp; Windows</h3>
  <p>Weatherstripping, Replacements<br>Glass and Screen Installation and Repair,<br>Install locksets</p>
  <div class="abs btn-dark">Read More</div>
</article>

<footer class="abs footer">
  <div class="abs brand-mark">Bright Lane Fixers</div>
  <p class="abs about-text">Serving the Millbrook, and surrounding areas.<br>One Name, One number, One call means one service for fast timely quotes, home repairs and updates for you and/or your clients.</p>

  <h4 style="left:382px">NAVIGATION</h4>
  <ul class="abs links">
    <li class="active">Home</li><li>Pages</li><li>Services</li><li>Blog</li><li>Gallery</li><li>Contact Us</li>
  </ul>

  <h4 style="left:572px">CONTACT DETAILS</h4>
  <div class="abs detail" style="top:82px">
    <div class="ico"><svg width="10" height="13" viewBox="0 0 11 14"><path d="M5.5 0A5.5 5.5 0 0 0 0 5.5C0 9.5 5.5 14 5.5 14S11 9.5 11 5.5A5.5 5.5 0 0 0 5.5 0z" fill="#fff"/><circle cx="5.5" cy="5.3" r="2" fill="#ff2424"/></svg></div>
    <div><b>HARBOR ROW OFFICE</b><span>Diam nummy Rich,<br>eulioumm tincidunt ut laor<br>laoreet dolore magna<br>123456</span></div>
  </div>
  <div class="abs detail" style="top:186px;align-items:center">
    <div class="ico"><svg width="12" height="12" viewBox="0 0 12 12"><path d="M2.5 0.5l2 2.5-1.2 1.5c.8 1.6 2 2.8 3.6 3.6L8.4 7l2.6 2-1 2.2C5 11 1 7 .6 2z" fill="#fff"/></svg></div>
    <span>555-201-4477</span>
  </div>
  <div class="abs detail" style="top:228px;align-items:center">
    <div class="ico"><svg width="13" height="10" viewBox="0 0 13 10"><rect x="0.5" y="0.5" width="12" height="9" fill="#fff"/><path d="M.5.5l6 5 6-5" fill="none" stroke="#ff2424" stroke-width="1.2"/></svg></div>
    <span>Mara@brightlanefixers.com</span>
  </div>

  <h4 style="left:849px">SUBSCRIBE NEWSLETTER</h4>
  <p class="abs newsletter">Enter your email address for our mailing list to keep your self our latest updated.</p>
  <div class="abs email-box">Email Address</div>
  <div class="abs signup">SIGN UP</div>
</footer>
<div class="abs copyright">Copyright © 2007 - 2016 BRIGHT LANE FIXERS All Rights Reserved</div>

</body>
</html>
```